Pull Up Banner - Recruitment Company

We would like a design for a pull up banner.

For context: we are a recruitment business. We specialise in helping people in healthcare industry to find jobs in Australia.

I have come up with several ideas and text for the banner. Feel free to use the following as you see appropriate:

- Our logo (see attached)
- 'Healthcare Recruitment Agency'
- Some sort of imagine / cartoon of medical professionals (ie. doctor, nurse, physiotherapist, speech pathologist). A cartoon is more friendly than committing to a photo
- 'Empowering your next career move'
- 'Discover tailored opportunities based on your career preferences'
- Dot points (allied health, nursing, medical imaging)
- Contact info at the bottom including our website (www.quellstaffing.com.au, our Instagram handle @quellstaffing, Mobile: XXXX XXX XXX. The title section for contact information could be 'Get in touch:'

Feel free to submit a couple of designs and we can merge aspects that look good on your designs and find the perfect fit.
Thank you
Updates

Hello,

Thank you for your initial submissions to this project. I appreciate the time you've invested.

After reviewing the first attempt, I'd like to share some feedback and initial observations:

- Professionalism and engagement: Is the overall appearance of the banner professional? It's crucial that we have a high-quality design as this will represent our business.

- Image selection: The image (whether cartoon or real people) appears quite generic. Please consider submitting the banner with a few different photos in the middle for us to choose from. Ensure the image is a good fit and not simply a generic stock photo.

- Contact section: Kindly remove the phone number; we no longer wish to include it on the banner. Instead, please include our website (www.quellstaffing.com.au) and Instagram handle (@quellstaffing).

- Color scheme: White, black, and red/pink are preferred, or alternatively, blue. However, please avoid incorporating too many different colors as it may detract from the professional appearance.

We will be printing the design on a banner and require it to look professional and engaging.

Thank you once again for your submissions. I hope the feedback provided above is helpful.

Warm regards,

Target Market(s)

Allied Health Australia

Font styles to use
Serif

Colors
0054AA
0677BA
7BADD7
CADEEF
E8F1F8
0094D4
00A9DD
6FCCEA
C7EBF8
E9F6FB
EB3D1F
EC4F4E
F09395
F8D3D4
FCEDEE

```html
<!DOCTYPE html>
<html lang="en">
<head>
<meta charset="utf-8">
<title>Quell Staffing – Healthcare Recruitment Pull Up Banner</title>
<link rel="stylesheet" href="https://fonts.googleapis.com/css2?family=Ubuntu:wght@500;700&family=Crimson+Pro:wght@700&family=Lexend:wght@300&display=swap">
<style>
  :root {
    --green: #0e7d3b;
    --navy: #1b3f73;
    --ink: #111111;
    --deep-ink: #13294b;
    --white: #ffffff;
    --page: #ffffff;
  }
  html, body {
    margin: 0;
    padding: 0;
    width: 847px;
    height: 1200px;
    overflow: hidden;
    background: var(--page);
  }
  .canvas {
    position: relative;
    width: 847px;
    height: 1200px;
    overflow: hidden;
  }
  .banner {
    position: absolute;
    left: 168px;
    top: 0;
    width: 510px;
    height: 1200px;
    background: var(--white);
    overflow: hidden;
    box-shadow: 0 0 6px rgba(0,0,0,0.35);
  }
  .shape { position: absolute; left: 0; top: 0; }
  .brand {
    position: absolute;
    left: 142px;
    top: 48px;
    font-family: "Ubuntu", sans-serif;
    font-weight: 700;
    color: var(--ink);
    font-size: 28px;
    letter-spacing: 1px;
    line-height: 1;
  }
  .brand-rule {
    position: absolute;
    left: 142px;
    top: 100px;
    width: 114px;
    height: 7px;
    background: var(--ink);
  }
  .headline {
    position: absolute;
    left: 48px;
    top: 170px;
    margin: 0;
    font-family: "Ubuntu", sans-serif;
    font-weight: 500;
    font-size: 72px;
    line-height: 63px;
    color: var(--white);
    white-space: nowrap;
  }
  .tagline-band {
    position: absolute;
    left: 0;
    top: 390px;
    width: 510px;
    height: 46px;
    background: var(--navy);
    display: flex;
    align-items: center;
    justify-content: center;
    font-family: "Crimson Pro", serif;
    font-weight: 700;
    font-size: 30px;
    color: var(--white);
    white-space: nowrap;
  }
  .team-photo {
    position: absolute;
    left: 0;
    top: 446px;
    width: 510px;
    height: 312px;
    background:
      linear-gradient(180deg, rgba(150,154,156,0.9) 0%, rgba(150,154,156,0) 45%),
      linear-gradient(90deg, #4e86b8 0%, #5b90c0 25%, #e6ecf1 45%, #eef2f5 55%, #7aa9d3 72%, #8fb6da 85%, #dfe6ec 100%);
  }
  .intro {
    position: absolute;
    left: 0;
    top: 776px;
    width: 510px;
    margin: 0;
    text-align: center;
    font-family: "Crimson Pro", serif;
    font-weight: 700;
    font-size: 32px;
    line-height: 29px;
    color: var(--deep-ink);
    white-space: nowrap;
  }
  .specialties {
    position: absolute;
    left: 0;
    top: 850px;
    width: 510px;
    height: 141px;
    background: var(--green);
    overflow: hidden;
  }
  .specialty {
    position: absolute;
    font-family: "Ubuntu", sans-serif;
    font-weight: 700;
    font-size: 32px;
    line-height: 1;
    color: var(--white);
    white-space: nowrap;
    display: flex;
    align-items: center;
    gap: 9px;
  }
  .specialty svg { display: block; }
  .specialty-imaging { left: 164px; top: 22px; }
  .specialty-allied { left: 56px; top: 57px; }
  .specialty-nursing { left: 298px; top: 57px; }
  .cta {
    position: absolute;
    left: 175px;
    top: 1026px;
    width: 281px;
    height: 58px;
    box-sizing: border-box;
    border: 1.5px solid var(--navy);
    border-radius: 29px;
    background: var(--white);
    display: flex;
    align-items: center;
    justify-content: center;
    padding-left: 30px;
    font-family: "Ubuntu", sans-serif;
    font-weight: 700;
    font-size: 29px;
    color: var(--green);
  }
  .social-mark {
    position: absolute;
    left: 126px;
    top: 1095px;
    width: 31px;
    height: 31px;
    border-radius: 7px;
    background: var(--white);
  }
  .contact {
    position: absolute;
    left: 54px;
    font-family: "Lexend", sans-serif;
    font-weight: 300;
    font-size: 23px;
    line-height: 1;
    color: var(--white);
    white-space: nowrap;
    display: flex;
    align-items: center;
    gap: 7px;
  }
  .contact-social { top: 1134px; }
  .contact-web { top: 1162px; letter-spacing: 4px; }
</style>
</head>
<body>
<div class="canvas">
  <section class="banner">
    <svg class="shape" width="510" height="1200" viewBox="0 0 510 1200" aria-hidden="true">
      <path fill="var(--green)" d="M0,50 C20,110 60,138 130,142 C300,152 490,170 510,252 L510,380 L0,380 Z"/>
      <path fill="var(--navy)" d="M0,1148 C30,1085 90,1054 150,1056 C235,1058 290,1112 380,1110 C450,1108 498,1058 510,1010 L510,1200 L0,1200 Z"/>
    </svg>

    <div class="brand">QUELL STAFFING</div>
    <div class="brand-rule"></div>

    <h1 class="headline">Healthcare<br>Recruitment<br>Agency</h1>

    <div class="tagline-band">Empowering your next career move</div>

    <div class="team-photo" role="img" aria-label="Photo of a team of healthcare professionals in blue scrubs and white coats, wearing masks, reviewing a clipboard together in a grey corridor"></div>

    <p class="intro">Discover tailored opportunities<br>based on your career preferences</p>

    <div class="specialties">
      <svg class="shape" width="510" height="141" viewBox="0 0 510 141" aria-hidden="true">
        <path fill="var(--white)" d="M0,80 C40,35 100,25 140,40 C90,35 30,70 4,141 L0,141 Z"/>
      </svg>
      <div class="specialty specialty-imaging">Medical Imaging
        <svg width="14" height="16" viewBox="0 0 14 16" aria-hidden="true"><path fill="var(--white)" d="M14,0 L14,16 L0,8 Z"/></svg>
      </div>
      <div class="specialty specialty-allied">
        <svg width="14" height="16" viewBox="0 0 14 16" aria-hidden="true"><path fill="var(--white)" d="M0,0 L14,8 L0,16 Z"/></svg>Allied Health
      </div>
      <div class="specialty specialty-nursing">
        <svg width="14" height="16" viewBox="0 0 14 16" aria-hidden="true"><path fill="var(--white)" d="M0,0 L14,8 L0,16 Z"/></svg>Nursing
      </div>
    </div>

    <div class="cta">GET IN TOUCH</div>

    <div class="social-mark" aria-hidden="true"></div>

    <div class="contact contact-social">@ quellstaffing</div>
    <div class="contact contact-web">
      <svg width="20" height="20" viewBox="0 0 24 24" aria-hidden="true"><g fill="none" stroke="var(--white)" stroke-width="1.3"><circle cx="12" cy="12" r="10"/><ellipse cx="12" cy="12" rx="4.5" ry="10"/><line x1="2" y1="12" x2="22" y2="12"/><line x1="4" y1="7" x2="20" y2="7"/><line x1="4" y1="17" x2="20" y2="17"/></g></svg>www.quellstaffing.com.au
    </div>
  </section>
</div>
</body>
</html>
```